Counsel Atelier

we need all the matirials for the office to speak with the internet site
www.corvenfirm-example.com

look stilish and modern yet very respecteble

our logo needs to be our logo and some times

just the letters " Corven " done nicely.

We need to send e mails with a design

Firm paper

and our gmail products to look nice when we use google docs

so we need a place for

lawers names and

the corven

and logo

and address

and some one to help us do it all

Target Market(s)

Big firms

Industry/Entity Type

Law Firm

Font styles to use
Serif

Requirements
Must have
• Rememrable
• Different yet respectable
• For multi languages
• LAW
• B
• LAWYERS
• BOUTIQUE
Nice to have
• Clean Design
• impressive
• i put on a new card i liked
• We should not put any decorations and beautiful logo
• it's against the law for lawyers
• I have a card that proves that we are smart and boutiques
• This card that I attached as an example
• Makes you little work, and certainly - apart from everyone
• Would love this design idea
• The numbers stated hiding it from top to bottom
• I put my real information integration profile
• The thing is that people should enlighten other options and other card
• This should be accessible designer fee changes
• Still very respectable and serious
• it needs to say among other creative stuff
• Counsel atelier CORVEN
• MARCUS TELLION
• 052-7196205
• 1@corvenfirm-example.com
• www.corvenfirm-example.com
• but any smart idea
Should not have
• We have a problam
• It turns out that the law of the Bar Association in
• Our country
• Do not allow to put the firm logo on business cards
• Or office paper
• the logo can only be letters and names
• So we should convey the idea of all sorts of areas along
• As we tried with our logo
• Through the letters themselves
• And their integration with each other

```html
<!DOCTYPE html>
<html lang="en">
<head>
<meta charset="utf-8">
<title>Counsel Atelier – Business Cards</title>
<link rel="stylesheet" href="https://fonts.googleapis.com/css2?family=Arimo:wght@400;700&display=swap">
<style>
  :root {
    --backdrop: #ececec;
    --card-front: #000000;
    --card-back: #b3b3b3;
    --ink-light: #f2f2f2;
    --ink-dark: #1c1c1c;
    --ink-body: #1f1f1f;
    --card-shadow: rgba(0, 0, 0, 0.18);
  }
  * { margin: 0; padding: 0; box-sizing: border-box; }
  html, body {
    width: 1200px;
    height: 1126px;
    overflow: hidden;
  }
  body {
    background: var(--backdrop);
    font-family: "Arimo", Arial, sans-serif;
    position: relative;
  }
  .card {
    position: absolute;
    width: 786px;
    height: 435px;
    box-shadow: 0 3px 8px var(--card-shadow);
  }
  .card--front {
    left: 212px;
    top: 136px;
    background: var(--card-front);
  }
  .card--back {
    left: 223px;
    top: 622px;
    background: var(--card-back);
  }
  .wordmark {
    position: absolute;
    font-weight: 700;
    font-size: 46px;
    line-height: 36px;
    letter-spacing: 4px;
    text-transform: uppercase;
    white-space: nowrap;
  }
  .wordmark__line { display: block; }
  .wordmark__line--second { padding-left: 150px; }
  .card--front .wordmark {
    left: 313px;
    top: 302px;
    color: var(--ink-light);
  }
  .card--back .wordmark {
    left: 302px;
    top: 48px;
    color: var(--ink-dark);
  }
  .contact {
    position: absolute;
    left: 44px;
    top: 290px;
    color: var(--ink-body);
  }
  .contact__name {
    font-size: 22px;
    letter-spacing: 0.5px;
    line-height: 26px;
  }
  .contact__role {
    font-size: 18px;
    letter-spacing: 1px;
    line-height: 24px;
  }
  .contact__details {
    margin-top: 32px;
    font-size: 19px;
    line-height: 24px;
    white-space: nowrap;
  }
</style>
</head>
<body>
  <section class="card card--front" aria-label="Business card front">
    <div class="wordmark">
      <span class="wordmark__line">Counsel</span>
      <span class="wordmark__line wordmark__line--second">Atelier</span>
    </div>
  </section>

  <section class="card card--back" aria-label="Business card back">
    <div class="wordmark">
      <span class="wordmark__line">Counsel</span>
      <span class="wordmark__line wordmark__line--second">Atelier</span>
    </div>
    <div class="contact">
      <p class="contact__name">MARCUS TELLION</p>
      <p class="contact__role">Founder &amp; Owner</p>
      <p class="contact__details">052-7196205 | 1@corvenfirm-example.com | www.corvenfirm-example.com</p>
    </div>
  </section>
</body>
</html>
```